K.R.O.U.B.S. Content Framework Infographic

I am looking to take my basic infographic to the next level. I need to to translate the content marketing concept that is outlined in the uploaded file. I have attached the content and the image I would like used. I am not stuck on the colors represented in the image but do want to see a variety of options.

Target Market(s)

Companies that are looking for a content marketing strategy, SEO Agencies, marketing agencies

Industry/Entity Type

Digital marketing, SEO

Font styles to use
Other font styles liked:
• arial, calibri are fine

Colors
0054AA
0677BA
7BADD7
CADEEF
E8F1F8
0094D4
00A9DD
6FCCEA
C7EBF8
E9F6FB
00AB8E
00BBA5
67D7C9
C6EFE9
E9F9F6
59FF00
82FF00
B8FF75
E3FFCB
F4FFEA
EE7325
F08F49
F5BC92
FAE3D3
FDF4ED
EB3D1F
EC4F4E
F09395
F8D3D4
FCEDEE

Requirements
Must have
• The image that I provided with the content breakdown with section connectors to the image
Nice to have
• a few different way to present the data

```html
<!DOCTYPE html>
<html lang="en">
<head>
<meta charset="utf-8">
<title>K.R.O.U.B.S. Content Framework Infographic</title>
<link href="https://fonts.googleapis.com/css2?family=Roboto:wght@300;400;500;700&display=swap" rel="stylesheet">
<style>
  :root{
    --page-grey:#a2a6aa;
    --cream:#fdf4ee;
    --cream-light:#fef8f3;
    --peach:#fbe2d4;
    --pink-band:#f6d3d3;
    --title-blue:#1c73b9;
    --ink:#3b3b3b;
    --ink-dark:#1f2a44;
    --gold:#d3ab38;
    --blue:#2a88c6;
    --orange:#ef8a3a;
    --red:#e94b4b;
    --teal:#17a985;
    --olive:#7b9537;
    --icon-light:#f4f1ea;
    --icon-yellow:#f4c025;
  }
  *{box-sizing:border-box;margin:0;padding:0}
  html,body{width:1200px;height:3600px;overflow:hidden}
  body{background:var(--page-grey);font-family:"Roboto",Arial,sans-serif;color:var(--ink);position:relative}
  .panel{position:absolute;left:119px;top:109px;width:964px;height:3391px;
    background:linear-gradient(180deg,var(--cream) 0%,var(--cream-light) 40%,var(--cream) 100%)}
  .band{position:absolute;left:119px;top:1294px;width:964px;height:391px;background:var(--pink-band)}
  .footer{position:absolute;left:119px;top:3328px;width:964px;height:172px;background:var(--peach)}
  .abs{position:absolute}

  .title{left:166px;top:150px;font-size:92px;line-height:91px;font-weight:300;color:var(--title-blue);letter-spacing:-1px;white-space:nowrap}
  .title b{font-weight:700}
  .title .k{color:var(--gold);font-weight:500}.title .r{color:var(--blue);font-weight:500}
  .title .o{color:var(--orange);font-weight:500}.title .u{color:var(--red);font-weight:500}
  .title .bb{color:var(--teal);font-weight:500}.title .s{color:var(--olive);font-weight:500}
  .title .dot{color:var(--blue);font-weight:500}

  .brand{display:flex;align-items:center;gap:10px;font-weight:700;color:var(--olive);font-size:34px;white-space:nowrap}
  .brand .mark{width:26px;height:26px;background:var(--olive)}
  .brand-top{left:812px;top:462px}
  .brand-foot{left:500px;top:3410px;font-size:32px}

  .kicker{left:170px;top:530px;font-size:32px;font-weight:500;color:var(--ink)}
  .body{font-size:21.5px;line-height:29px;font-weight:300;color:var(--ink)}
  .body strong{font-weight:500}
  .intro-a{left:170px;top:593px;width:215px}
  .intro-b{left:170px;top:758px;width:290px}

  .formats{left:501px;top:601px;width:531px;height:490px;background:#f9dccd;border-radius:10px}
  .format-row{position:absolute;left:30px;display:flex;align-items:center;gap:22px}
  .format-icon{width:102px;height:76px;border-radius:6px;flex:none}
  .format-row .body{width:370px}

  .breakdown{left:170px;top:1131px;font-size:31px;line-height:42px;font-weight:500;color:var(--ink)}
  .breakdown .acr{color:var(--gold)}

  .sec-head{left:168px;font-size:37px;font-weight:500;white-space:nowrap}
  .tile{left:170px;width:160px;height:151px;border-radius:4px}
  .tile svg{display:block;width:160px;height:151px}
  .sec-text{left:345px;font-size:21px;line-height:29px}
  .sec-text.multimedia{width:540px}
  .sec-text.engagement{width:565px}
  .sec-text.experience{width:600px}
  .sec-text.expertise{width:630px}
  .sec-text.authority{width:640px}
  .sec-text.trust{width:640px}

  .contact{left:170px;top:3365px;font-size:20px;line-height:30px;color:var(--ink-dark)}
  .contact b{font-weight:700}
  .site{left:806px;top:3410px;font-size:34px;font-weight:700;color:var(--ink-dark)}
</style>
</head>
<body>
  <div class="panel"></div>
  <div class="band"></div>
  <div class="footer"></div>

  <h1 class="abs title">Putting <span class="k">K</span><span class="dot">.</span><span class="r">R</span><span class="dot">.</span><span class="o">O</span><span class="dot">.</span><span class="u">U</span><span class="dot">.</span><span class="bb">B</span><span class="dot">.</span><span class="s">S</span><span class="dot">.</span><br>on the bone for the<br><b>User &amp; Searchwise</b><br>to chew on</h1>

  <div class="abs brand brand-top"><span class="mark"></span>Summit Search</div>

  <h2 class="abs kicker">In SEO content is still king</h2>

  <p class="abs body intro-a">What has changed with content is not the content but the <strong>delivery</strong> of that content.</p>
  <svg class="abs" style="left:350px;top:658px" width="100" height="78" viewBox="0 0 100 78" role="img" aria-label="Document delivery icon">
    <rect x="38" y="2" width="58" height="72" rx="4" fill="#8fd3ea"/>
    <g stroke="#2a88c6" stroke-width="4"><line x1="50" y1="20" x2="86" y2="20"/><line x1="50" y1="34" x2="86" y2="34"/><line x1="50" y1="48" x2="86" y2="48"/><line x1="50" y1="62" x2="86" y2="62"/><line x1="2" y1="30" x2="20" y2="30"/><line x1="6" y1="44" x2="24" y2="44"/></g>
    <polygon points="24,26 44,37 24,48" fill="#e94b4b"/>
  </svg>
  <p class="abs body intro-b">People these days are consuming content in so many different places &amp; formats that it makes it difficult to create engaging <strong>content that ranks and converts</strong>.</p>

  <svg class="abs" style="left:182px;top:980px" width="100" height="112" viewBox="0 0 100 112" role="img" aria-label="Rating bar chart">
    <rect x="4" y="50" width="30" height="60" fill="#17a985"/>
    <rect x="34" y="30" width="32" height="80" fill="#2a88c6"/>
    <rect x="66" y="62" width="30" height="48" fill="#e94b4b"/>
    <circle cx="18" cy="30" r="9" fill="#f4c025"/><circle cx="50" cy="12" r="10" fill="#f4c025"/><circle cx="82" cy="36" r="9" fill="#f4c025"/>
  </svg>
  <svg class="abs" style="left:325px;top:978px" width="124" height="114" viewBox="0 0 124 114" role="img" aria-label="Content exchange icon">
    <rect x="8" y="40" width="50" height="70" rx="4" fill="#8fd3ea"/>
    <rect x="66" y="2" width="54" height="76" rx="4" fill="#8fd3ea"/>
    <g stroke="#2a88c6" stroke-width="4"><line x1="18" y1="60" x2="48" y2="60"/><line x1="18" y1="74" x2="48" y2="74"/><line x1="18" y1="88" x2="48" y2="88"/><line x1="76" y1="20" x2="110" y2="20"/><line x1="76" y1="34" x2="110" y2="34"/><line x1="76" y1="48" x2="110" y2="48"/><line x1="76" y1="62" x2="110" y2="62"/></g>
    <path d="M52 10 H24 V28" stroke="#17a985" stroke-width="6" fill="none"/>
    <path d="M76 104 H104 V88" stroke="#17a985" stroke-width="6" fill="none"/>
  </svg>

  <div class="abs formats">
    <div class="format-row" style="top:28px">
      <div class="format-icon" style="background:linear-gradient(#fff 0 70%,#f4c025 70%);border:3px solid #e2e2e2" role="img" aria-label="Webpage icon"></div>
      <p class="body">Some people prefer to continue reading <strong>webpages</strong> to find the information they are looking for.</p>
    </div>
    <div class="format-row" style="top:140px">
      <div class="format-icon" style="background:linear-gradient(180deg,#8fd3ea 55%,#17a985 55%);border:4px solid #9a9a9a" role="img" aria-label="Picture icon"></div>
      <p class="body">Some prefer to see the <strong>pictures</strong> because they are more visual than contextual.</p>
    </div>
    <div class="format-row" style="top:252px">
      <div class="format-icon" style="background:linear-gradient(180deg,#f4c025 50%,#2a88c6 50%)" role="img" aria-label="Video icon"></div>
      <p class="body">Others would prefer to just watch video on VidStream or other <strong>online video platforms</strong>.</p>
    </div>
    <div class="format-row" style="top:365px">
      <div class="format-icon" style="background:radial-gradient(circle at 50% 40%,#e94b4b 0 18%,#cfcfcf 19% 40%,transparent 41%),linear-gradient(90deg,transparent 0 12%,#2a88c6 12% 22%,transparent 22% 78%,#2a88c6 78% 88%,transparent 88%)" role="img" aria-label="Podcast microphone icon"></div>
      <p class="body">In some cases it is more of an auditory way such as <strong>podcast &amp; streaming radio platforms</strong>.</p>
    </div>
  </div>

  <p class="abs breakdown">This infographic will breakdown how<br>all of the pieces fit together to get<br><span class="acr">K.R.O.U.B.S</span> on the bone of content.</p>
  <div class="abs" style="left:777px;top:1113px;width:258px;height:154px;border-radius:24px;background:linear-gradient(120deg,#ef8a3a,#d3ab38 30%,#e94b4b 55%,#17a985 75%,#2a88c6)" role="img" aria-label="Scattered framework pieces illustration"></div>

  <svg class="abs" style="left:0;top:0" width="1200" height="3600" viewBox="0 0 859 2576" preserveAspectRatio="none">
    <defs>
      <linearGradient id="pieceGrad" x1="0" x2="1">
        <stop offset="0" stop-color="#ef8a3a"/><stop offset=".3" stop-color="#17a985"/><stop offset=".55" stop-color="#d3ab38"/><stop offset=".72" stop-color="#e94b4b"/><stop offset="1" stop-color="#2a88c6"/>
      </linearGradient>
    </defs>
    <rect x="125" y="1000" width="445" height="228" rx="40" fill="url(#pieceGrad)" role="img" aria-label="Pig illustration divided into six framework cuts: expertise, trust, multimedia, authority, experience, engagement"/>
    <g fill="none" stroke-width="6" stroke-linejoin="round" stroke-linecap="round">
      <path d="M390 1020 V996 H645 V1277 H122" stroke="#d3ab38"/>
      <path d="M520 1083 H663 V1499 H122" stroke="#2a88c6"/>
      <path d="M430 1135 L470 1170 H685 V1670 H122" stroke="#e94b4b"/>
      <path d="M200 1060 V955 H705 V1843 H122" stroke="#ef8a3a"/>
      <path d="M310 1170 V1202 H722 V2017 H122" stroke="#17a985"/>
      <path d="M280 1040 V973 H740 V2190 H122" stroke="#7b9537"/>
    </g>
  </svg>

  <h3 class="abs sec-head" style="top:1731px;color:var(--gold)">Multimedia</h3>
  <div class="abs tile" style="top:1781px;background:var(--gold)" role="img" aria-label="Media types icon">
    <svg viewBox="0 0 160 151" aria-hidden="true">
      <rect x="34" y="28" width="42" height="42" rx="3" fill="var(--icon-light)"/>
      <polygon points="48,37 66,49 48,61" fill="var(--red)"/>
      <rect x="84" y="28" width="42" height="42" rx="3" fill="var(--icon-yellow)"/>
      <polygon points="94,42 102,42 112,34 112,64 102,56 94,56" fill="var(--icon-light)"/>
      <rect x="34" y="78" width="42" height="42" rx="3" fill="var(--blue)"/>
      <circle cx="50" cy="106" r="6" fill="var(--icon-light)"/><rect x="54" y="86" width="4" height="20" fill="var(--icon-light)"/>
      <rect x="84" y="78" width="42" height="42" rx="3" fill="var(--teal)"/>
      <polygon points="84,120 98,100 108,110 116,102 126,114 126,120" fill="var(--icon-light)"/>
    </svg>
  </div>
  <p class="abs body sec-text multimedia" style="top:1797px">Consists of <strong>infographics, specific images, embedded videos and other types content aside from the written word</strong>. By doing this you provide the same content to audiences that differ based on how they choose to consume content. Online content marketing with multimedia is <strong>highly engaging</strong> as it presents desired information in a multifaceted but direct and timely manner.</p>

  <h3 class="abs sec-head" style="top:2041px;color:var(--blue)">Engagement</h3>
  <div class="abs tile" style="top:2091px;background:var(--blue)" role="img" aria-label="Browser window with reactions icon">
    <svg viewBox="0 0 160 151" aria-hidden="true">
      <rect x="38" y="28" width="84" height="66" rx="4" fill="var(--icon-light)"/>
      <rect x="38" y="28" width="84" height="14" rx="4" fill="#8fd3ea"/>
      <circle cx="47" cy="35" r="2.5" fill="var(--red)"/><circle cx="55" cy="35" r="2.5" fill="var(--icon-yellow)"/><circle cx="63" cy="35" r="2.5" fill="var(--teal)"/>
      <rect x="30" y="84" width="34" height="30" rx="4" fill="var(--red)"/>
      <path d="M47 108 l-9-9 a5 5 0 0 1 9-5 a5 5 0 0 1 9 5z" fill="var(--icon-light)"/>
      <rect x="64" y="90" width="30" height="28" rx="4" fill="var(--icon-yellow)"/>
      <rect x="94" y="84" width="34" height="30" rx="4" fill="var(--teal)"/>
      <path d="M111 91 v16 M103 99 h16" stroke="var(--icon-light)" stroke-width="4"/>
    </svg>
  </div>
  <p class="abs body sec-text engagement" style="top:2107px">Essential for views and conversion as it keeps <strong>readers locked in on content</strong> to the point that they are more likely to move through the website experience and at least <strong>consider the value offered in the minutes, hours, days, and weeks that follow their website visit.</strong></p>

  <h3 class="abs sec-head" style="top:2281px;color:var(--red)">Experience</h3>
  <div class="abs tile" style="top:2333px;background:var(--red)" role="img" aria-label="Briefcase with star icon">
    <svg viewBox="0 0 160 151" aria-hidden="true">
      <rect x="62" y="36" width="30" height="16" rx="4" fill="none" stroke="#9a9a9a" stroke-width="6"/>
      <rect x="32" y="50" width="90" height="66" rx="6" fill="#c9c9c9"/>
      <rect x="32" y="50" width="90" height="26" rx="6" fill="var(--icon-light)"/>
      <rect x="68" y="72" width="18" height="12" rx="2" fill="#6f6f6f"/>
      <polygon points="120,20 126,33 140,34 129,43 133,57 120,49 107,57 111,43 100,34 114,33" fill="var(--icon-yellow)"/>
    </svg>
  </div>
  <p class="abs body sec-text experience" style="top:2349px">In short means that Searchwise values <strong>firsthand or life experience of the author</strong> on the topic a page is about. It is important because often searchers want to know <strong>first-hand information</strong> before they decide to purchase something or use a certain service.</p>

  <h3 class="abs sec-head" style="top:2523px;color:var(--orange)">Expertise</h3>
  <div class="abs tile" style="top:2575px;background:var(--orange)" role="img" aria-label="Expert medal icon">
    <svg viewBox="0 0 160 151" aria-hidden="true">
      <polygon points="66,88 56,124 70,116 78,128 84,94" fill="var(--red)"/>
      <polygon points="94,88 104,124 90,116 82,128 76,94" fill="var(--red)"/>
      <circle cx="80" cy="68" r="32" fill="var(--icon-yellow)"/>
      <circle cx="80" cy="68" r="22" fill="var(--icon-light)"/>
      <polygon points="80,52 85,63 97,64 88,72 91,84 80,78 69,84 72,72 63,64 75,63" fill="var(--blue)"/>
    </svg>
  </div>
  <p class="abs body sec-text expertise" style="top:2591px">Refers to the <strong>content writer's level of knowledge or skill</strong> in a specific subject area that is relevant to the user's search query. High-quality content should be created by someone with <strong>relevant expertise in the topic being discussed</strong>.</p>

  <h3 class="abs sec-head" style="top:2765px;color:var(--teal)">Authoritativeness</h3>
  <div class="abs tile" style="top:2818px;background:var(--teal)" role="img" aria-label="Shield with tick icon">
    <svg viewBox="0 0 160 151" aria-hidden="true">
      <path d="M80 26 L112 38 V66 C112 88 96 104 80 112 C64 104 48 88 48 66 V38 Z" fill="var(--red)"/>
      <path d="M64 66 L76 78 L98 54" fill="none" stroke="var(--icon-yellow)" stroke-width="8" stroke-linecap="round" stroke-linejoin="round"/>
      <path d="M30 96 L48 118 H66" fill="none" stroke="var(--icon-light)" stroke-width="10" stroke-linecap="round" stroke-linejoin="round"/>
      <path d="M130 96 L112 118 H94" fill="none" stroke="var(--icon-light)" stroke-width="10" stroke-linecap="round" stroke-linejoin="round"/>
    </svg>
  </div>
  <p class="abs body sec-text authority" style="top:2834px">Refers to the <strong>credibility of the content and the website</strong> it is hosted on. Authoritativeness can be established through the <strong>quality of the content, the site's reputation, author's reputation, external links &amp; content citations, and the credentials of the content creator</strong>.</p>

  <h3 class="abs sec-head" style="top:3006px;color:var(--olive)">Trustworthiness</h3>
  <div class="abs tile" style="top:3059px;background:var(--olive)" role="img" aria-label="Agreement with tick icon">
    <svg viewBox="0 0 160 151" aria-hidden="true">
      <circle cx="80" cy="52" r="26" fill="var(--icon-yellow)"/>
      <path d="M68 52 L77 61 L93 44" fill="none" stroke="var(--icon-light)" stroke-width="7" stroke-linecap="round" stroke-linejoin="round"/>
      <rect x="30" y="90" width="100" height="24" rx="12" fill="#f08f49"/>
      <path d="M60 102 H100" stroke="var(--icon-light)" stroke-width="5" stroke-linecap="round"/>
    </svg>
  </div>
  <p class="abs body sec-text trust" style="top:3075px">Is the final result of doing all of the above. If you can write content that is helpful, knowledge, first hand based on experience from someone who is an expert in their field, you get the <strong>trust of users consuming your content</strong>. If you can gain the user's trust about your content, Searchwise and other search engines will “Trust” you and will <strong>provide you with the organic visibility we all strive for</strong>.</p>

  <p class="abs contact"><b>555-014-2290</b><br>2210 Ridgeline Ave Ste 4<br>Aspen Falls, CO 80000</p>
  <div class="abs brand brand-foot"><span class="mark"></span>Summit Search</div>
  <p class="abs site">SUMMIT.AGENCY</p>
</body>
</html>
```